New AI Company Needs a Powerpoint

We are a new type of AI company called KestrelMind. Our AI uses human inspired approaches and put the human on the center of all our solutions. We need a standard company powerpoint design to use with potential investors, customers and partners to introduce our company and explain how the approach we take to AI is very different than others.
We want a design that is clean, modern, and playful. We do not want it to look overly robotic or cliche techy. Our mission is to remind the world that technology is a tool to be used to enhance and assist not to replace real humans.
We want a design that can show boring things (like financial info) in engaging ways.

Please use colors in logo variations along with a vibrant complementary color palette of your choosing,

Industry/Entity Type

Technology

Font styles to use
Sans Serif
Other font styles liked:
• Opensans

Colors
0054AA
0677BA
7BADD7
CADEEF
E8F1F8
0094D4
00A9DD
6FCCEA
C7EBF8
E9F6FB
00AB8E
00BBA5
67D7C9
C6EFE9
E9F9F6
59FF00
82FF00
B8FF75
E3FFCB
F4FFEA

Requirements
Must have
• Must incorporate logo colors and style

```html
<!DOCTYPE html>
<html lang="en">
<head>
<meta charset="utf-8">
<title>KestrelMind — Company Deck Overview</title>
<link href="https://fonts.googleapis.com/css2?family=Montserrat:wght@500;600;700;800&family=Open+Sans:ital,wght@0,400;0,600;0,700;1,400&display=swap" rel="stylesheet">
<style>
  :root{
    --stage:#57575a;
    --navy:#0f3566;
    --blue:#0054AA;
    --blue-mid:#0677BA;
    --sky:#0094D4;
    --teal:#00AB8E;
    --teal-bright:#00BBA5;
    --ink:#1f2630;
    --body:#4b525c;
    --rule:#d9dde2;
    --gray-bar:#6d6a6a;
    --white:#ffffff;
  }
  *{box-sizing:border-box;margin:0;padding:0}
  html,body{width:1200px;height:1200px;overflow:hidden;background:var(--stage)}
  body{position:relative;font-family:"Open Sans",Arial,sans-serif}
  .brand-hero{position:absolute;left:0;top:120px;width:1200px;text-align:center;
    font-family:"Montserrat",Arial,sans-serif;font-weight:600;font-size:44px;letter-spacing:3px;color:var(--white)}
  .slide{position:absolute;width:366px;height:205px;background:var(--white);overflow:hidden}
  .abs{position:absolute}
  .photo{position:absolute}
  .eyebrow{position:absolute;font-size:5.6px;color:var(--blue-mid)}
  .heading{position:absolute;font-family:"Montserrat",Arial,sans-serif;font-weight:700;color:var(--ink);font-size:10.5px;line-height:12.5px}
  .para{position:absolute;font-size:4.9px;line-height:8.2px;color:var(--body)}
  .footer-rule{position:absolute;left:6px;right:6px;top:188px;height:0.6px;background:var(--rule)}
  .page-num{position:absolute;left:6px;top:193px;width:10px;height:10px;background:var(--sky);color:#fff;font-size:4.5px;text-align:center;line-height:10px}
  .copyright{position:absolute;left:20px;top:195px;font-size:4.3px;color:#7a818b}
  .footer-brand{position:absolute;right:8px;top:195px;font-family:"Montserrat",Arial,sans-serif;font-weight:700;font-size:4px;color:var(--blue)}
  .item-title{font-family:"Montserrat",Arial,sans-serif;font-weight:700;font-size:5.4px;color:var(--ink)}
  .item-text{font-size:4.7px;line-height:6.2px;color:var(--body)}
  .icon-box{position:absolute;width:22px;height:22px;border:0.8px solid var(--blue-mid);border-radius:3px}
  .icon-box.filled{background:var(--blue-mid);border:none}
  .icon-box::after{content:"";position:absolute;left:6px;top:6px;width:9px;height:9px;border:0.8px solid var(--blue-mid);border-radius:50%}
  .icon-box.filled::after{border-color:#fff}
</style>
</head>
<body>

<div class="brand-hero">KESTRELMIND</div>

<!-- 1 Title -->
<section class="slide slide-title" style="left:35px;top:300px;background:var(--navy)">
  <div class="photo" role="img" aria-label="Team working at laptops, tinted deep blue" style="inset:0;background:linear-gradient(135deg,#16406f,#0e3260 55%,#143a66)"></div>
  <svg class="abs" style="left:0;top:0" width="366" height="205">
    <circle cx="362" cy="30" r="30" fill="none" stroke="var(--blue-mid)" stroke-width="9"/>
    <circle cx="10" cy="198" r="55" fill="none" stroke="var(--blue-mid)" stroke-width="10" opacity=".8"/>
  </svg>
  <div class="abs" style="left:0;width:366px;top:63px;text-align:center;font-family:Montserrat,sans-serif;font-weight:700;font-size:6px;color:#fff">KESTRELMIND</div>
  <div class="abs" style="left:0;width:366px;top:78px;text-align:center;font-family:Montserrat,sans-serif;font-weight:800;font-size:18.5px;letter-spacing:1.3px;color:var(--teal-bright)">PRESENTATION TITLE</div>
  <div class="abs" style="left:80px;width:206px;top:102px;text-align:center;font-size:5px;line-height:8px;color:#fff">Lorem ipsum dolor sit amet, consectetur adipiscing elit, sed do eiusmod tempor incididunt ut labore et dolore magna.</div>
  <div class="abs" style="left:149px;top:126px;width:68px;height:10px;border-radius:5px;background:#fff;text-align:center;font-size:4.4px;line-height:10px;font-weight:700;font-style:italic;color:var(--blue)">Presented by: Ava Rowan</div>
</section>

<!-- 2 About -->
<section class="slide" style="left:417px;top:300px">
  <div class="photo" role="img" aria-label="Colleagues collaborating around laptops at a wooden table" style="left:20px;top:0;width:133px;height:173px;border-radius:0 0 8px 8px;background:linear-gradient(160deg,#8a6a50,#4d4038 60%,#2f2a28)"></div>
  <div class="abs" style="left:153px;top:5px;width:8px;height:24px;background:var(--blue-mid)"></div>
  <div class="eyebrow" style="left:181px;top:50px">About Us</div>
  <div class="abs" style="left:181px;top:62px;width:3.5px;height:22px;background:var(--teal)"></div>
  <div class="heading" style="left:189px;top:61px">Building Responsible<br>AI for Everyone.</div>
  <div class="para" style="left:181px;top:92px;width:160px">Lorem ipsum dolor sit amet, consectetur adipiscing elit, sed do eiusmod tempor incididunt uti labore et dolore magna aliquea. Ut enim ad minim veniam, iquis nostrud exercitation ullamcoiu laboris nisi ut aliquip exlea commodo consequat. Duis autelore irure dolor in reprehenderit in voluptate velit esse cillum venia dolore eu fugiat nulla pariatur. Excepteur sint occaeca tnostrud cupidatat non proident, sunt in culpa qui officia deserunt.</div>
  <div class="footer-rule"></div><div class="page-num">2</div>
  <div class="copyright">© 2022 KestrelMind. All Rights Reserved.</div><div class="footer-brand">KESTRELMIND</div>
</section>

<!-- 3 Algorithms -->
<section class="slide" style="left:798px;top:300px">
  <svg class="abs" style="left:0;top:0" width="366" height="205"><circle cx="348" cy="45" r="52" fill="none" stroke="var(--blue-mid)" stroke-width="11"/></svg>
  <div class="photo" role="img" aria-label="Desktop monitor showing lines of code in a bright office" style="left:216px;top:17px;width:126px;height:156px;background:linear-gradient(170deg,#cfd3d6,#9aa3aa 55%,#5a6168)"></div>
  <div class="abs" style="left:211px;top:18px;width:0.8px;height:56px;background:var(--teal)"></div>
  <div class="abs" style="left:204px;top:158px;width:12px;height:20px;background:var(--blue-mid)"></div>
  <div class="eyebrow" style="left:18px;top:38px">Ideas, Planning, Strategy.</div>
  <div class="heading" style="left:18px;top:50px;font-size:9.6px;line-height:11.5px">Based on state-of-the-art<br>Machine Learning Algorithms</div>
  <div class="para" style="left:18px;top:80px;width:152px">Lorem ipsum dolor sit amet, consectetur adipiscing elit, sed do eiusmod tempor incididunt uti labore et dolore magnael aliqua. Ut enim ad minim veniam, quis nostrud exercitation ullamco laboris nisi ut aliquip ex ea commodo consequat.</div>
  <div class="para" style="left:18px;top:117px;width:152px">Duis aute irure dolorina reprehenderit in voluptate velit qui esse cillum dolore eu fugiat nulla pariatur. Excepteur sinted occaecat cupidatat non proident, sunt in culpa qui officiasa deserunt mollit anim id est laborum.</div>
  <div class="footer-rule"></div><div class="page-num">3</div>
  <div class="copyright">© 2022 KestrelMind. All Rights Reserved.</div><div class="footer-brand">KESTRELMIND</div>
</section>

<!-- 4 Model -->
<section class="slide" style="left:35px;top:520px">
  <svg class="abs" style="left:0;top:0" width="180" height="190">
    <circle cx="61" cy="58" r="32" fill="var(--blue-mid)"/>
    <path d="M128 66 A70 70 0 0 1 150 120" fill="none" stroke="var(--sky)" stroke-width="0.8"/>
    <circle cx="107" cy="39" r="2.5" fill="none" stroke="var(--sky)" stroke-width="0.8"/>
    <circle cx="96" cy="35" r="1.5" fill="#aaa"/>
    <circle cx="36" cy="112" r="2.5" fill="var(--teal)"/>
    <circle cx="41" cy="125" r="4" fill="none" stroke="var(--blue-mid)" stroke-width="0.9"/>
  </svg>
  <div class="photo" role="img" aria-label="Smiling woman in glasses looking at her phone" style="left:34px;top:42px;width:118px;height:118px;border-radius:50%;background:radial-gradient(circle at 45% 40%,#e7e4e1,#a59d96 60%,#6f6a66)"></div>
  <div class="eyebrow" style="left:186px;top:39px">It's About Planning for The Future</div>
  <div class="heading" style="left:186px;top:50px">The Machine<br>Comprehension Model</div>
  <div class="para" style="left:186px;top:85px;width:152px">Lorem ipsum dolor sit amet, consectetur adipiscing elit, sed do eiusmod tempor incididunt uti labore et dolore magnael aliqua. Ut enim ad minim veniam, quis nostrud exercitation ullamco laboris nisi ut aliquip ex ea commodo consequat.</div>
  <div class="abs" style="left:186px;top:124px;width:150px;height:31px;background:var(--blue-mid);border-radius:2px">
    <div class="abs" style="left:8px;top:7px;width:17px;height:17px;border:0.8px solid #fff;border-radius:3px"></div>
    <div class="abs" style="left:34px;top:5px;width:0.6px;height:21px;background:#8fbde0"></div>
    <div class="abs" style="left:42px;top:8px;font-size:4.9px;line-height:8px;color:#fff">We build services for you from initial<br>sketches to the final production.</div>
  </div>
  <div class="footer-rule"></div><div class="page-num">4</div>
  <div class="copyright">© 2022 KestrelMind. All Rights Reserved.</div><div class="footer-brand">KESTRELMIND</div>
</section>

<!-- 5 Solution -->
<section class="slide" style="left:417px;top:520px">
  <div class="abs" style="left:20px;top:126px;width:146px;height:51px;background:var(--blue-mid);border-radius:0 0 6px 6px"></div>
  <div class="photo" role="img" aria-label="Diverse team meeting around an office table with laptops" style="left:29px;top:28px;width:129px;height:129px;background:linear-gradient(160deg,#d9dad6,#9c948a 55%,#5e574f)"></div>
  <div class="abs" style="left:23px;top:60px;width:0.8px;height:50px;background:var(--teal)"></div>
  <div class="abs" style="left:163px;top:28px;width:0.8px;height:40px;background:var(--teal)"></div>
  <div class="eyebrow" style="left:200px;top:28px">Our Solution</div>
  <div class="heading" style="left:200px;top:40px">We Continue to Evolve<br>The Solution</div>
  <div class="abs" style="left:200px;top:68px;width:18px;height:0.8px;background:var(--teal)"></div>
  <div class="icon-box filled" style="left:197px;top:79px;width:25px;height:25px"></div>
  <div class="abs" style="left:230px;top:81px;width:120px"><div class="item-title">Unique Ideas</div><div class="item-text">Porta lorem mollis aliquam ut porttitor leo a. Vel pharetra vel turpis nunc.</div></div>
  <div class="icon-box filled" style="left:197px;top:114px;width:25px;height:25px"></div>
  <div class="abs" style="left:230px;top:116px;width:120px"><div class="item-title">Inovative Solution</div><div class="item-text">Porta lorem mollis aliquam ut porttitor leo a. Vel pharetra vel turpis nunc.</div></div>
  <div class="icon-box filled" style="left:197px;top:150px;width:25px;height:25px"></div>
  <div class="abs" style="left:230px;top:151px;width:120px"><div class="item-title">Personal Approach</div><div class="item-text">Porta lorem mollis aliquam ut porttitor leo a. Vel pharetra vel turpis nunc.</div></div>
  <div class="footer-rule"></div><div class="page-num">5</div>
  <div class="copyright">© 2022 KestrelMind. All Rights Reserved.</div><div class="footer-brand">KESTRELMIND</div>
</section>

<!-- 6 Services -->
<section class="slide" style="left:798px;top:520px">
  <div class="abs" style="left:22px;top:14px;width:20px;height:10px;background:var(--blue-mid)"></div>
  <div class="photo" role="img" aria-label="Man in denim shirt working on a laptop at a desk" style="left:0;top:25px;width:122px;height:148px;background:linear-gradient(160deg,#6c7478,#3e4a55 55%,#25303a)"></div>
  <div class="abs" style="left:121px;top:25px;width:75px;height:0.8px;background:var(--teal)"></div>
  <div class="abs" style="left:126px;top:95px;width:0.8px;height:40px;background:var(--teal)"></div>
  <div class="eyebrow" style="left:150px;top:28px">Service Areas</div>
  <div class="heading" style="left:150px;top:39px">Explore Our Services</div>
  <div class="para" style="left:150px;top:61px;width:196px">Lorem ipsum dolor sit amet, consectetur adipiscing elit, sed do eiusmod tempor incididunt uti labore et dolore magnael aliqua. Ut enim ad minim veniam, quis nostrud exercitation ullamco laboris nisi ut aliquip ex ea commodo consequat.</div>
  <div class="icon-box" style="left:150px;top:107px"></div>
  <div class="abs" style="left:179px;top:108px;width:66px"><div class="item-title">Insert text here</div><div class="item-text">Porta lorem mollis aliqua utporttitor leo phareta.</div></div>
  <div class="icon-box" style="left:252px;top:107px"></div>
  <div class="abs" style="left:281px;top:108px;width:66px"><div class="item-title">Insert text here</div><div class="item-text">Porta lorem mollis aliqua utporttitor leo phareta.</div></div>
  <div class="icon-box" style="left:150px;top:144px"></div>
  <div class="abs" style="left:179px;top:145px;width:66px"><div class="item-title">Insert text here</div><div class="item-text">Porta lorem mollis aliqua utporttitor leo phareta.</div></div>
  <div class="icon-box" style="left:252px;top:144px"></div>
  <div class="abs" style="left:281px;top:145px;width:66px"><div class="item-title">Insert text here</div><div class="item-text">Porta lorem mollis aliqua utporttitor leo phareta.</div></div>
  <div class="footer-rule"></div><div class="page-num">6</div>
  <div class="copyright">© 2022 KestrelMind. All Rights Reserved.</div><div class="footer-brand">KESTRELMIND</div>
</section>

<!-- 7 Financials -->
<section class="slide" style="left:35px;top:740px">
  <div class="heading" style="left:0;width:366px;top:11px;text-align:center">Financial Projections</div>
  <div class="abs" style="left:172px;top:29px;width:22px;height:0.9px;background:var(--teal)"></div>
  <svg class="abs chart" style="left:0;top:0" width="200" height="170" font-family="Open Sans, sans-serif" font-size="4.4" fill="#555">
    <g stroke="#e1e3e6" stroke-width="0.5">
      <line x1="30" y1="63" x2="185" y2="63"/><line x1="30" y1="77" x2="185" y2="77"/>
      <line x1="30" y1="90" x2="185" y2="90"/><line x1="30" y1="104" x2="185" y2="104"/>
      <line x1="30" y1="118" x2="185" y2="118"/><line x1="30" y1="131" x2="185" y2="131"/>
      <line x1="30" y1="145" x2="185" y2="145"/>
      <line x1="30" y1="145" x2="40" y2="139"/><line x1="30" y1="63" x2="40" y2="53"/>
    </g>
    <g text-anchor="end">
      <text x="22" y="64">3</text><text x="22" y="78">2.5</text><text x="22" y="91">2</text>
      <text x="22" y="105">1.5</text><text x="22" y="119">1</text><text x="22" y="132">0.5</text><text x="22" y="146">0</text>
    </g>
    <rect x="43" y="104" width="13" height="41" fill="var(--blue)"/><polygon points="56,104 59,101 59,142 56,145" fill="#003f82"/><polygon points="43,104 46,101 59,101 56,104" fill="#2a6fc0"/>
    <rect x="80" y="77" width="13" height="68" fill="var(--blue-mid)"/><polygon points="93,77 96,74 96,142 93,145" fill="#05609a"/><polygon points="80,77 83,74 96,74 93,77" fill="#3a96cf"/>
    <rect x="117" y="90" width="13" height="55" fill="var(--teal)"/><polygon points="130,90 133,87 133,142 130,145" fill="#008a72"/><polygon points="117,90 120,87 133,87 130,90" fill="#3bc7ae"/>
    <rect x="154" y="72" width="13" height="73" fill="var(--gray-bar)"/><polygon points="167,72 170,69 170,142 167,145" fill="#4e4b4b"/><polygon points="154,72 157,69 170,69 167,72" fill="#8c8989"/>
    <g text-anchor="middle"><text x="51" y="155">Category 1</text><text x="88" y="155">Category 2</text><text x="125" y="155">Category 3</text><text x="162" y="155">Category 4</text></g>
  </svg>
  <div class="abs item-title" style="left:199px;top:51px;font-size:6.2px">Chart Description</div>
  <div class="para" style="left:199px;top:63px;width:142px;text-align:justify;line-height:7.7px">Lorem ipsum dolor sit amet, consectetuer adipiscing elit. Aenean commodo ligula hh eget dolor. Aenean massa. Cum sociis tygb natoque penatibus et magnis dis parturient montes, nascetur saf ridiculus mus. Donec dsa quam felis, ultricies nec, pellentesque eu, naedr pretium quis, sem. Nulla gd consequat massa quis enim. Donec pede justo, fringilla vel, aliquet nec, vulputate</div>
  <div class="abs" style="left:199px;top:125px;width:6px;height:6px;background:var(--blue)"></div>
  <div class="abs item-text" style="left:212px;top:124px">Insert Text In Here</div>
  <div class="abs" style="left:266px;top:125px;width:6px;height:6px;background:var(--teal-bright)"></div>
  <div class="abs item-text" style="left:279px;top:124px">Insert Text In Here</div>
  <div class="abs" style="left:199px;top:138px;width:6px;height:6px;background:var(--blue-mid)"></div>
  <div class="abs item-text" style="left:212px;top:137px">Insert Text In Here</div>
  <div class="abs" style="left:266px;top:138px;width:6px;height:6px;background:var(--gray-bar)"></div>
  <div class="abs item-text" style="left:279px;top:137px">Insert Text In Here</div>
  <div class="footer-rule"></div><div class="page-num">7</div>
  <div class="copyright">© 2022 KestrelMind. All Rights Reserved.</div><div class="footer-brand">KESTRELMIND</div>
</section>

<!-- 8 Section break -->
<section class="slide" style="left:417px;top:740px;background:var(--blue-mid)">
  <svg class="abs" style="left:0;top:0" width="366" height="205"><circle cx="355" cy="28" r="45" fill="none" stroke="var(--sky)" stroke-width="13"/></svg>
  <div class="abs" style="left:36px;top:40px;width:131px;height:133px;background:var(--teal-bright)"></div>
  <div class="photo" role="img" aria-label="Smiling woman holding a cup while working on a laptop" style="left:32px;top:38px;width:129px;height:131px;background:linear-gradient(150deg,#c9d6d8,#8fa7ab 50%,#5e7479)"></div>
  <div class="abs" style="left:28px;top:110px;width:0.8px;height:40px;background:#9fd0ec"></div>
  <div class="abs" style="left:186px;top:87px;font-family:Montserrat,sans-serif;font-weight:800;font-size:16.5px;letter-spacing:.6px;color:#fff">SECTION BREAK</div>
  <div class="abs" style="left:186px;top:110px;width:160px;font-size:5px;line-height:8px;color:#fff">Lorem ipsum dolor sit amet, consectetur adipiscing elit, sed do eiusmod tempor incididunt uti labore et dolore magnael.</div>
  <div class="abs" style="left:186px;top:129px;width:40px;height:0.9px;background:#fff"></div>
  <div class="abs" style="left:228px;top:129px;width:4px;height:0.9px;background:#fff"></div>
  <div class="abs" style="left:234px;top:129px;width:4px;height:0.9px;background:#fff"></div>
</section>

<!-- 9 Organizations -->
<section class="slide" style="left:798px;top:740px">
  <div class="photo" role="img" aria-label="Hands typing on a laptop, deep blue tinted background" style="left:0;top:0;width:366px;height:103px;background:linear-gradient(120deg,#1a4479,#0f3262 60%,#1b4a80)"></div>
  <div class="photo" role="img" aria-label="Hands on a laptop keyboard with glowing network graphics" style="left:21px;top:20px;width:108px;height:150px;background:linear-gradient(160deg,#2a5a8f,#7aa2c7 55%,#d9e2ea)"></div>
  <div class="abs" style="left:16px;top:131px;width:0.8px;height:40px;background:var(--sky)"></div>
  <div class="abs" style="left:100px;top:172px;width:28px;height:0.8px;background:var(--teal)"></div>
  <div class="heading" style="left:147px;top:25px;color:#fff;font-size:10.4px">How AI Technology Can Help<br>Organizations</div>
  <div class="para" style="left:147px;top:62px;width:200px;color:#fff">Lorem ipsum dolor sit amet, consectetur adipiscing elit, sed do eiusmod tempor incididunt uti labore et dolore magnael aliqua. Ut enim ad minim veniam, quis nostrud exercitation ullamco laboris nisi ut aliquip ex.</div>
  <div class="icon-box" style="left:143px;top:113px"></div>
  <div class="abs" style="left:171px;top:114px;width:74px"><div class="item-title">Insert text here</div><div class="item-text">Porta lorem mollis aliquam ut porttitor leo pharetra.</div></div>
  <div class="icon-box" style="left:250px;top:113px"></div>
  <div class="abs" style="left:279px;top:114px;width:74px"><div class="item-title">Insert text here</div><div class="item-text">Porta lorem mollis aliquam ut porttitor leo pharetra.</div></div>
  <div class="icon-box" style="left:143px;top:146px"></div>
  <div class="abs" style="left:171px;top:147px;width:74px"><div class="item-title">Insert text here</div><div class="item-text">Porta lorem mollis aliquam ut porttitor leo pharetra.</div></div>
  <div class="icon-box" style="left:250px;top:146px"></div>
  <div class="abs" style="left:279px;top:147px;width:74px"><div class="item-title">Insert text here</div><div class="item-text">Porta lorem mollis aliquam ut porttitor leo pharetra.</div></div>
  <div class="footer-rule"></div><div class="page-num">9</div>
  <div class="copyright">© 2022 KestrelMind. All Rights Reserved.</div><div class="footer-brand">KESTRELMIND</div>
</section>

<!-- 10 Adaptive -->
<section class="slide" style="left:35px;top:960px">
  <svg class="abs" style="left:0;top:0" width="366" height="205"><polygon points="242,0 366,0 366,124" fill="var(--blue-mid)"/></svg>
  <div class="photo" role="img" aria-label="Developer desk with monitors of code under purple light" style="left:217px;top:20px;width:128px;height:162px;background:linear-gradient(165deg,#2b2f6e,#5a3a8c 50%,#2a1f3f)"></div>
  <div class="abs" style="left:212px;top:45px;width:0.8px;height:45px;background:var(--teal)"></div>
  <div class="abs" style="left:350px;top:125px;width:0.8px;height:45px;background:var(--teal)"></div>
  <div class="abs" style="left:212px;top:170px;width:12px;height:12px;background:var(--blue-mid)"></div>
  <div class="heading" style="left:21px;top:44px;font-size:10.8px;line-height:13px">From Artificial Intelligence<br>to Adaptive Intelligence</div>
  <div class="abs" style="left:21px;top:75px;width:17px;height:0.9px;background:var(--teal)"></div>
  <div class="para" style="left:21px;top:81px;width:150px">Lorem ipsum dolor sit amet, consectetur adipiscing elit, sed do eiusmod tempor incididunt uti labore et dolore magnael aliqua. Ut enim ad minim veniam, quis nostrud exercitation ullamco labioris nisi ut aliuip exea commodo velit consequat. Duis aute irure dolorina reprehenderit in voluptate velit qui esse cillum dolore eu fugiat nulla pariatur.</div>
  <div class="abs" style="left:21px;top:135px;width:56px;height:12px;border:0.8px solid var(--teal);border-radius:6px;text-align:center;font-size:5.4px;line-height:10.5px;color:var(--blue-mid)">READ MORE</div>
  <div class="footer-rule"></div><div class="page-num">10</div>
  <div class="copyright">© 2022 KestrelMind. All Rights Reserved.</div><div class="footer-brand">KESTRELMIND</div>
</section>

<!-- 11 Team -->
<section class="slide" style="left:417px;top:960px">
  <div class="eyebrow" style="left:0;width:366px;top:15px;text-align:center">Our Team</div>
  <div class="heading" style="left:0;width:366px;top:26px;text-align:center">Team of Experts</div>
  <div class="para" style="left:40px;width:286px;top:50px;text-align:center">Lorem ipsum dolor sit amet, consectetur adipiscing elit, sed do eiusmod tempor incididunt uti labore et dolore magnael aliqua. Ut enim ad minim veniam, quis nostrud exercitation ullamco laboris nisi ut aliuip.</div>

  <div class="photo" role="img" aria-label="Portrait of a team member in a suit" style="left:37px;top:82px;width:59px;height:59px;background:linear-gradient(160deg,#9fb3c4,#4f5f70)"></div>
  <div class="abs" style="left:33px;top:141px;width:63px;height:0.8px;background:var(--teal)"></div>
  <div class="abs" style="left:33px;width:67px;top:151px;text-align:center"><div class="item-title" style="color:var(--blue-mid)">Owen Hale</div><div class="item-text" style="font-style:italic">General Manager</div></div>

  <div class="photo" role="img" aria-label="Portrait of a smiling team member" style="left:114px;top:82px;width:59px;height:59px;background:linear-gradient(160deg,#c7bfb2,#7f7466)"></div>
  <div class="abs" style="left:110px;top:141px;width:63px;height:0.8px;background:var(--teal)"></div>
  <div class="abs" style="left:107px;width:73px;top:151px;text-align:center"><div class="item-title" style="color:var(--blue-mid)">Nora Quinlan</div><div class="item-text" style="font-style:italic">Chief Operating Officer</div></div>

  <div class="photo" role="img" aria-label="Portrait of a smiling team member" style="left:192px;top:82px;width:59px;height:59px;background:linear-gradient(160deg,#c4c6c8,#6a6f74)"></div>
  <div class="abs" style="left:188px;top:141px;width:63px;height:0.8px;background:var(--teal)"></div>
  <div class="abs" style="left:183px;width:77px;top:151px;text-align:center"><div class="item-title" style="color:var(--blue-mid)">Felix Marsh</div><div class="item-text" style="font-style:italic">Senior Digital Strategist</div></div>

  <div class="photo" role="img" aria-label="Portrait of a team member with long hair" style="left:269px;top:82px;width:59px;height:59px;background:linear-gradient(160deg,#d9c7b8,#9a8472)"></div>
  <div class="abs" style="left:265px;top:141px;width:63px;height:0.8px;background:var(--teal)"></div>
  <div class="abs" style="left:262px;width:70px;top:151px;text-align:center"><div class="item-title" style="color:var(--blue-mid)">Iris Bellamy</div><div class="item-text" style="font-style:italic">Managing Director</div></div>

  <div class="footer-rule"></div><div class="page-num">11</div>
  <div class="copyright">© 2022 KestrelMind. All Rights Reserved.</div><div class="footer-brand">KESTRELMIND</div>
</section>

<!-- 12 Contact -->
<section class="slide" style="left:798px;top:960px">
  <div class="abs" style="left:0;top:0;width:70px;height:205px;background:var(--blue-mid)"></div>
  <div class="abs" style="left:146px;top:22px;width:37px;height:127px;border:0.8px solid var(--teal-bright);border-left:none"></div>
  <div class="abs" style="left:146px;top:22px;width:0.8px;height:6px;background:var(--teal-bright)"></div>
  <div class="abs" style="left:108px;top:18px;width:12px;height:0.8px;background:var(--sky)"></div>
  <div class="abs" style="left:122px;top:18px;width:3px;height:0.8px;background:var(--sky)"></div>
  <div class="photo" role="img" aria-label="Support agent wearing a headset at a laptop" style="left:22px;top:29px;width:148px;height:147px;background:linear-gradient(160deg,#eef1f3,#b9c2ca 55%,#3c4a63)"></div>
  <div class="abs" style="left:218px;top:58px;font-family:Montserrat,sans-serif;font-weight:700;font-size:5.4px;color:var(--ink)">KESTRELMIND</div>
  <div class="abs" style="left:218px;top:71px;font-family:Montserrat,sans-serif;font-weight:700;font-size:11.5px;letter-spacing:.4px;color:var(--sky)">Contact Info</div>
  <div class="abs" style="left:218px;top:88px;width:20px;height:0.9px;background:var(--teal)"></div>
  <div class="abs item-title" style="left:220px;top:100px;color:var(--blue-mid);font-size:5px">Address</div>
  <div class="abs item-text" style="left:253px;top:99px;line-height:7.8px;font-size:5px">: 48 Harbor Lane, Suite 2,<br>&nbsp;&nbsp;Portland, OR, USA.</div>
  <div class="abs item-title" style="left:220px;top:122px;color:var(--blue-mid);font-size:5px">Phone</div>
  <div class="abs item-text" style="left:253px;top:121px;font-size:5px">: +1 (0) 555 010 2468</div>
  <div class="abs item-title" style="left:220px;top:135px;color:var(--blue-mid);font-size:5px">Email</div>
  <div class="abs item-text" style="left:253px;top:134px;font-size:5px">: hello@kestrelmind.example</div>
  <div class="abs item-title" style="left:220px;top:148px;color:var(--blue-mid);font-size:5px">Website</div>
  <div class="abs item-text" style="left:253px;top:147px;font-size:5px">: www.kestrelmind.example</div>
</section>

</body>
</html>
```